Dane Morrow films- wedding and event films company website. DESKTOP AND MOBILE

We need a website for a high-end wedding and event film production company. Looking for a very modern and elegant design. my old website is www.danemorrowfilms.example

I like the "white/black/rose gold" color scheme of my logo.

really looking for a sleek modern design the breaths professional and artistic.

Target Market(s)

wedding and event films.

Industry/Entity Type

Film Production

Number of Pages Required

5+ page

Colors

Designer to choose colors to be used in the design.

Requirements
Must have
• website name will be www.danemorrowfilms.example
• tagline is "CINEMATIC STORIES ABOUT YOU"
• sections: HOME, CONTACT, ABOUT, FILMS, BLOG
• You can see my old website at danemorrowfilms.example
• Website about section:
• Dane Morrow Films was Established with the basis of truly cinematic and artistic films in mind. Dane and his team routinely travel the globe documenting weddings and events for high profile clients and discerning couples. Dane was born and raised in Maui Hawaii and has a unique approach to his films that embody the essence of a Hollywood film. Dane has spent the last 10 years traveling the world documenting corporate events and weddings with multiple Award winning production companies. In 2017 Dane decided to establish his own brand “Dane Morrow films” that will take everything he has learned with his past experiences and push it to the next level. Aside from his personal achievements, Dane is extremely passionate about his craft and always looks forward to handcrafting beautiful wedding/event films for his clients. The style of work is non-traditional and the day of filming is extremely unobtrusive (as we are looking for natural-candid/ raw emotions).
• If you are looking for the best price in town, we are probably not the best option, but if you’re looking for the best quality and peace of mind on your wedding day, then you’re in the right place. Dane Morrow Films is a boutique studio that only accepts a limited number of assignments per year. Inquire early to ensure availability.
• LINKS TO VIMEO VIDEOS THAT WILL BE IN THE "FILMS' SECTION.
• BRENT FILM TRAILER - https://clipvault.example/508114362
• BRENT FEATURE FILM - https://clipvault.example/617392048
• JUNE AND ROB'S WEDDING - https://clipvault.example/724958160
• DRONE DEMO REEL - https://clipvault.example/841576203
• WEDDING INDUSTRY EVENT PARTY - https://clipvault.example/962304817/a8d3e7b21c
• images that you can use on site are here: https://brigittolsenimages.proofbox.example/gallery/nora&felix/
• password is: meadow

```html
<!DOCTYPE html>
<html lang="en">
<head>
<meta charset="utf-8">
<title>Dane Morrow Films — Cinematic Stories About You</title>
<link href="https://fonts.googleapis.com/css2?family=Poppins:wght@300;400;600&display=swap" rel="stylesheet">
<style>
  :root {
    --ink: #ffffff;
    --rose-gold: #e7935a;
    --rule: rgba(255,255,255,0.75);
    --shade-dark: #1f1712;
    --shade-mid: #4a3a30;
    --shade-light: #6d5a4d;
  }
  * { margin: 0; padding: 0; box-sizing: border-box; }
  html, body { width: 1200px; height: 668px; overflow: hidden; background: var(--shade-dark); }
  body { font-family: "Poppins", sans-serif; color: var(--ink); }

  .hero { position: relative; width: 1200px; height: 668px; overflow: hidden; }
  .hero-photo {
    position: absolute; inset: 0;
    background:
      radial-gradient(ellipse 320px 420px at 620px 360px, rgba(120,100,88,0.55), transparent 70%),
      radial-gradient(ellipse 260px 240px at 1020px 380px, rgba(150,130,115,0.35), transparent 70%),
      radial-gradient(ellipse 240px 300px at 150px 360px, rgba(140,118,100,0.35), transparent 70%),
      linear-gradient(180deg, var(--shade-dark) 0%, var(--shade-mid) 45%, var(--shade-light) 75%, var(--shade-mid) 100%);
  }

  .brand {
    position: absolute; left: 163px; top: 88px; width: 150px;
    text-align: center; font-weight: 400; color: var(--ink);
    text-transform: uppercase; line-height: 1;
  }
  .brand-main { display: block; font-size: 14px; letter-spacing: 1.5px; }
  .brand-sub { display: block; font-size: 8px; letter-spacing: 4px; margin-top: 5px; }

  .topbar {
    position: absolute; left: 393px; top: 40px;
    display: flex; align-items: center; font-size: 12px;
  }
  .topbar-email { font-weight: 300; margin-right: 16px; }
  .social { display: flex; gap: 16px; margin-right: 22px; }
  .social-dot { width: 8px; height: 8px; border-radius: 50%; background: var(--ink); }
  .social-dot.is-accent { background: var(--rose-gold); }
  .topbar-phone { font-weight: 600; letter-spacing: 0.3px; }

  .main-nav {
    position: absolute; left: 362px; top: 75px; width: 476px; height: 40px;
    border-top: 1px solid var(--rule); border-bottom: 1px solid var(--rule);
  }
  .main-nav ul { list-style: none; display: flex; height: 100%; align-items: center; padding-left: 47px; }
  .main-nav li { font-size: 15.5px; font-weight: 300; margin-right: 38px; letter-spacing: 0.2px; }
  .main-nav li.is-current { color: var(--rose-gold); }

  .hero-copy { position: absolute; left: 0; right: 0; top: 432px; text-align: center; }
  .tagline { font-size: 38px; font-weight: 300; letter-spacing: 0.8px; line-height: 1.2; }
  .testimonial { margin-top: 17px; font-size: 15px; font-weight: 300; line-height: 24px; }
  .cta {
    display: inline-block; margin-top: 20px; width: 128px; height: 33px; line-height: 31px;
    border: 1.5px solid var(--rose-gold); color: var(--rose-gold);
    font-size: 13px; font-weight: 300; letter-spacing: 0.3px; text-decoration: none;
  }

  .slider-control { position: absolute; }
  .prev { left: 28px; top: 316px; }
  .next { left: 1158px; top: 316px; }
  .fullscreen { left: 1152px; top: 357px; }
  .play { left: 1158px; top: 402px; }
</style>
</head>
<body>
<main class="hero">
  <div class="hero-photo" role="img" aria-label="Warm sepia-toned photo of a smiling bride and groom walking arm in arm down an outdoor wedding aisle, guests and white chairs softly blurred behind them"></div>

  <div class="brand">
    <span class="brand-main">Dane Morrow</span>
    <span class="brand-sub">Films</span>
  </div>

  <div class="topbar">
    <span class="topbar-email">dane@danemorrowfilms.example</span>
    <span class="social" aria-label="Social links">
      <span class="social-dot"></span>
      <span class="social-dot"></span>
      <span class="social-dot is-accent"></span>
    </span>
    <span class="topbar-phone">Call us: 808-555-0147</span>
  </div>

  <nav class="main-nav">
    <ul>
      <li class="is-current">HOME</li>
      <li>CONTACT</li>
      <li>ABOUT</li>
      <li>FILMS</li>
      <li>BLOG</li>
    </ul>
  </nav>

  <section class="hero-copy">
    <h1 class="tagline">Cinematic Stories About You</h1>
    <p class="testimonial">“Dane really is one of the best film makers in<br>Hawaii,&nbsp; great work Dane! We loved the film!” — Lena Harwood</p>
    <a class="cta" href="#contact">CONTACT US</a>
  </section>

  <svg class="slider-control prev" width="12" height="18" viewBox="0 0 12 18" aria-label="Previous slide"><polyline points="9,2 3,9 9,16" fill="none" stroke="#fff" stroke-width="1.6"/></svg>
  <svg class="slider-control next" width="12" height="18" viewBox="0 0 12 18" aria-label="Next slide"><polyline points="3,2 9,9 3,16" fill="none" stroke="#fff" stroke-width="1.6"/></svg>
  <svg class="slider-control fullscreen" width="26" height="26" viewBox="0 0 26 26" aria-label="Fullscreen">
    <circle cx="13" cy="13" r="12" fill="none" stroke="#fff" stroke-width="1.4"/>
    <path d="M9 17 L17 9 M13.5 9 H17 V12.5 M9 13.5 V17 H12.5" fill="none" stroke="#fff" stroke-width="1.4"/>
  </svg>
  <svg class="slider-control play" width="12" height="14" viewBox="0 0 12 14" aria-label="Play slideshow"><polygon points="2,2 10,7 2,12" fill="none" stroke="#fff" stroke-width="1.4"/></svg>
</main>
</body>
</html>
```